Tordo Brand Fuego Cut Jalapeños

Company Background Information:
Tordo Brand Farms is a family owned and operated business since 1981. Our Jalapeños are grown through sustainable practices environmentally socially and economically. We are a company based in Mexico looking to enter the U.S. and international retail market.
Packaging Design Description:
We manufacture Fuego Cut Jalapeño Peppers on a stand up pouch bag with a zipper. We currently are labeling as can be seen in attached picture, but I am looking for a design to be printed in the bag on both sides front and back that will stand out in the shelf of the retail market.
Attached are the photo files of the bag dimensions and the finished product with current label.
Requirements:
1. Logo: Tordo Brand (Attached in file)
2. Name of Product: Fuego Cut Jalapeño Peppers
3. Generic Nutrition Facts panel.
4. " Best Before: " (For expiration date purposes)
5. " Refrigerate after opening"
6. Ingredients: Jalapeño Peppers, Water, Vinegar, Salt, Oregano, Bay Leaf, Garlic, Thyme & Calcium Chloride
7. Net Wt. 16 oz
8. Generic Bar Code
9. Processed by: Empacadora Cerro Azufre S.A. de C.V.
Av. Quintero 482 Int. 3 Col. Centro
Guaymas, Son. Mexico
10. www.tordobrand.example
11. e-mail info@tordobrand.example
12. Phone: 52(987)654-3210
We would like a fresh appearance. Somewhat traditional. It is also directed towards a more economical market.
Target Market(s)
Our target market is mostly the latino population in the United States, the growing diversity of cultures in the US is helping people try different cuisines, spicy foods in our case.

```html
<!DOCTYPE html>
<html lang="en">
<head>
<meta charset="utf-8">
<title>Tordo Brand Fuego Cut Jalapeño Peppers</title>
<link rel="stylesheet" href="https://fonts.googleapis.com/css2?family=Archivo:wght@700;900&display=swap">
<style>
  :root {
    --page-bg: #ffffff;
    --pouch-green: #3f9d3f;
    --pouch-green-deep: #2a7f2f;
    --glow: rgba(255, 255, 255, 0.85);
    --title-green: #1f8a2a;
    --ink: #1a1a1a;
    --white: #ffffff;
    --flag-green: #2f9a35;
    --flag-red: #d8151b;
    --gold-dark: #9c6a22;
    --gold-mid: #d7ad5f;
    --gold-light: #f0d595;
  }
  * { margin: 0; padding: 0; box-sizing: border-box; }
  html, body {
    width: 900px;
    height: 1200px;
    overflow: hidden;
    background: var(--page-bg);
  }
  .canvas {
    position: relative;
    width: 900px;
    height: 1200px;
  }
  .pouch-front {
    position: absolute;
    left: 150px;
    top: 180px;
    width: 600px;
    height: 840px;
    background:
      radial-gradient(ellipse 260px 220px at 50% 26%, var(--glow), rgba(255,255,255,0) 100%),
      linear-gradient(180deg, var(--pouch-green) 0%, var(--pouch-green-deep) 100%);
    overflow: hidden;
  }
  .zip-band {
    position: absolute;
    left: 0; top: 0;
    width: 100%;
    height: 34px;
    background: var(--pouch-green-deep);
    opacity: 0.55;
  }
  .pouch-art {
    position: absolute;
    inset: 0;
    width: 600px;
    height: 840px;
  }
  .brand-name {
    position: absolute;
    top: 170px;
    left: 0;
    width: 100%;
    text-align: center;
    font-family: "Archivo", sans-serif;
    font-weight: 700;
    font-size: 56px;
    line-height: 1;
    color: var(--ink);
  }
  .product-cut {
    position: absolute;
    top: 528px;
    left: 0;
    width: 100%;
    text-align: center;
    font-family: "Archivo", sans-serif;
    font-weight: 700;
    font-size: 21px;
    color: var(--ink);
  }
  .product-name {
    position: absolute;
    top: 578px;
    left: 0;
    width: 100%;
    text-align: center;
    font-family: "Archivo", sans-serif;
    font-weight: 900;
    font-size: 56px;
    line-height: 0.98;
    color: var(--title-green);
    -webkit-text-stroke: 2px var(--white);
    paint-order: stroke fill;
  }
</style>
</head>
<body>
<main class="canvas">
  <section class="pouch-front">
    <div class="zip-band"></div>
    <svg class="pouch-art" viewBox="0 0 600 840" xmlns="http://www.w3.org/2000/svg">
      <defs>
        <linearGradient id="gold-banner" x1="0" y1="0" x2="1" y2="0">
          <stop offset="0" stop-color="var(--gold-dark)"/>
          <stop offset="0.45" stop-color="var(--gold-light)"/>
          <stop offset="0.7" stop-color="var(--gold-mid)"/>
          <stop offset="1" stop-color="var(--gold-dark)"/>
        </linearGradient>
        <linearGradient id="sliced-peppers" x1="0" y1="0" x2="1" y2="1">
          <stop offset="0" stop-color="#9cc77a"/>
          <stop offset="0.5" stop-color="#5f9f45"/>
          <stop offset="1" stop-color="#b9d99c"/>
        </linearGradient>
      </defs>
      <polygon class="frame-triangle" points="80,333 520,333 300,790" fill="var(--white)"/>
      <polygon class="stripe-green" points="100,345 130,345 300,700 300,752" fill="var(--flag-green)"/>
      <polygon class="stripe-red" points="500,345 470,345 300,700 300,752" fill="var(--flag-red)"/>
      <polygon class="product-photo" points="130,345 470,345 300,700" fill="url(#sliced-peppers)" role="img" aria-label="Photo of sliced green jalapeño pepper rings"/>
      <path class="label-strip" d="M150,522 Q300,548 450,522 L456,560 Q300,586 144,560 Z" fill="var(--white)" opacity="0.85"/>
      <path class="gold-banner" d="M124,560 Q300,600 476,560 L482,690 Q300,735 118,690 Z" fill="url(#gold-banner)"/>
    </svg>
    <div class="brand-name">Tordo Brand</div>
    <div class="product-cut">Fuego Cut</div>
    <h1 class="product-name">Jalapeño<br>Peppers</h1>
  </section>
</main>
</body>
</html>
```